Poster for a Burlesque event

We need to update our poster for the burlesque-event Velvet Lantern Revue in Norway (more than 800 guests).

After using different designers we still love the old one (http://velvetlanternrevue.example/wp-content/gallery/plakaterposters/2163769686_33c4d2680b_o.jpg) but it's very 2008.

We want to update this poster to 2013 but still keep the retro/vintage feeling, expression and main design.

We also would like to use the Crescent Moon as a "signature" for the poster. (Very sorry for saying this 4 hours after posting this job)

Size: 50x70cm will be the primary size

We're open to suggestion to any brilliant suggestion.

PS! We're a group of friends that arrange this event
Updates

Hi everybody saying yes to participate on this job.

I (Torvald) was now reminded by my collegues that we also would like to use the Crescent Moon as a "signature" for the poster if possible. 

Very sorry for saying this 4 hours after posting this job.

Regards 
Torvald
Velvet Lantern Revue

Hello,
Thank you so much in participating and contribute a design for a new poster for our event "Velvet Lantern Revue". After getting many contributions one designer came up with a design so perfect for our need that I choose to end the project ahead of time. She had, from our perspective, a perfect bland of vintage, burlesque and style that we sought for. 

I will provide feedback for all contributions.

Regards

Target Market(s)

People with an interest in the 1920 to 1940's... and burlesque

Industry/Entity Type

Event

Requirements
Must have
• This is the challenge... lots of text:

Velvet Lantern Revue proudly presents:
A night of carnival spectaculair
Silver Gull Jamboree
9th march 2013

Starring:
Rosa Quill ( Uk)
The Vamporettes with Miss Sssss ( NO)
Tango Fandango with Norwegian horns! (ESP)

Our own Le Chat Doré:
Belle Rêve Du Soir( Constantinople)

Scarlet Gin Joy Revue:
Miss Dora Sapphire ( NO)
Miss Hot Shot ( US)
Edmund Tallis ( UK)
Pablo Ignacio Fuentes de la Costa Marcel ( Arrggg..)
Velvet Sting ( NO)
Miss Greta ( NO)
Tova Oopsydaisy ( NO)
Miss Sunny Ribbon (NO)

Velvet Lantern Revue introducing:

Debutante Burlesque Showdown!
4 new burlesque sensassions strutting their stuff for the first time at THE SILVER GULL JAMBOREE

Be there or be squair
Stjernekroken, Lindeløkka 17

We do insist, dress to impress!
Doors open at 18.00.
Show start Rosa Quill at 19.00

CC:400,-
Tickets sold at velvetlanternrevue.example.
More information, VIP-tables, earlybirdtickets, etc : velvetlanternrevue.example.
20 år leg.plikt

(Bottom - logos for our sponsors ... not yet ready)
Nice to have
• We also would like to use the Crescent Moon as a "signature" for the poster. Since we also have absinth as an underlying theme, the colour green (absinth-green) would be prefered.

I do not know if a crescent moon and green is at all possible, but we are open for suggestion.

Please check out our homepage www.velvetlanternrevue.example

(the design will be updated but for now, we're focusing on the poster)

```html
<!DOCTYPE html>
<html lang="en">
<head>
<meta charset="utf-8">
<title>Silver Gull Jamboree – Velvet Lantern Revue</title>
<link href="https://fonts.googleapis.com/css2?family=Anton&family=Cinzel:wght@700&family=Great+Vibes&family=Oswald:wght@400;500;600&family=Playfair+Display:ital,wght@1,700&display=swap" rel="stylesheet">
<style>
  :root {
    --plum-deep: #1d0614;
    --plum: #5a1840;
    --mauve: #a0527f;
    --blush: #f3d6e6;
    --badge-pink: #e8327e;
    --ink-dark: #2a0a1f;
    --white: #ffffff;
    --muted: #b98aa6;
  }
  html, body { margin: 0; padding: 0; overflow: hidden; background: var(--plum-deep); }
  .poster {
    position: relative;
    width: 851px; height: 1200px; overflow: hidden;
    background:
      radial-gradient(ellipse 70% 45% at 50% 38%, rgba(255,230,245,.55) 0%, rgba(190,110,160,.35) 35%, rgba(0,0,0,0) 70%),
      linear-gradient(180deg, var(--plum) 0%, var(--mauve) 38%, #7a2c5c 62%, var(--plum-deep) 100%);
    font-family: "Oswald", sans-serif;
    color: var(--white);
    text-align: center;
  }
  .dancers {
    position: absolute; left: 150px; top: 0; width: 551px; height: 410px;
    background: radial-gradient(ellipse 55% 60% at 50% 45%, rgba(255,240,248,.9) 0%, rgba(240,200,225,.55) 45%, rgba(200,130,175,0) 80%);
  }
  .badge {
    position: absolute; left: 16px; top: 178px; width: 156px; height: 156px;
    border-radius: 50%; background: var(--badge-pink);
    display: flex; flex-direction: column; justify-content: center;
    font-weight: 600; font-size: 23px; line-height: 1.05; color: var(--white);
  }
  .tagline {
    position: absolute; left: 0; right: 0; top: 378px;
    font-family: "Playfair Display", serif; font-style: italic; font-weight: 700;
    font-size: 35px; padding-left: 120px; text-shadow: 0 2px 6px rgba(60,0,40,.5);
  }
  .event-title {
    position: absolute; left: -100px; right: -100px; top: 418px;
    font-family: "Anton", sans-serif; font-size: 120px; line-height: 1;
    letter-spacing: -2px; transform: scaleX(.82);
    text-shadow: 0 4px 10px rgba(60,0,40,.55);
  }
  .event-date {
    position: absolute; left: 0; right: 0; top: 600px;
    font-family: "Cinzel", serif; font-weight: 700; font-size: 27px;
    letter-spacing: 6px; color: var(--ink-dark);
  }
  .starring {
    position: absolute; left: 0; right: 0; top: 628px;
    font-family: "Great Vibes", cursive; font-size: 48px; line-height: 1;
  }
  .line { position: absolute; left: 0; right: 0; font-size: 14.5px; font-weight: 500; line-height: 1.3; white-space: nowrap; }
  .divider { position: absolute; left: 62px; right: 62px; top: 880px; border-top: 2px dotted rgba(255,255,255,.8); }
  .intro { font-size: 18.5px; }
  .fine-print { position: absolute; left: 0; right: 0; top: 1118px; font-size: 10px; color: var(--muted); }
  .web { position: absolute; left: 0; right: 0; top: 1152px; font-size: 22px; letter-spacing: 3px; }
</style>
</head>
<body>
<main class="poster">
  <div class="dancers" role="img" aria-label="Silhouettes of three burlesque dancers in a glowing spotlight"></div>

  <div class="badge">
    <span>Velvet Lantern</span><span>Revue</span><span>presents</span>
  </div>

  <p class="tagline" style="margin:0">A night of carnival spectaculair</p>
  <h1 class="event-title" style="margin:0">Silver Gull Jamboree</h1>
  <p class="event-date" style="margin:0">9TH MARCH 2013</p>
  <p class="starring" style="margin:0">Starring:</p>

  <p class="line" style="top:693px;margin:0">Rosa Quill ( Uk) • The Vamporettes with Miss Sssss ( NO) • Tango Fandango with Norwegian horns! (ESP)</p>

  <p class="line" style="top:735px;margin:0">Our own Le Chat Doré:</p>
  <p class="line" style="top:755px;margin:0">Belle Rêve Du Soir( Constantinople)</p>

  <p class="line" style="top:798px;margin:0">Scarlet Gin Joy Revue:</p>
  <p class="line" style="top:819px;margin:0">Miss Dora Sapphire ( NO) • Miss Hot Shot ( US) • Edmund Tallis ( UK) • Pablo Ignacio Fuentes de la Costa Marcel ( Arrggg..)</p>
  <p class="line" style="top:841px;margin:0">Velvet Sting ( NO) • Miss Greta ( NO) • Tova Oopsydaisy ( NO)• Miss Sunny Ribbon (NO)</p>

  <div class="divider"></div>

  <p class="line intro" style="top:903px;margin:0">Velvet Lantern Revue introducing:</p>
  <p class="line intro" style="top:929px;margin:0">Debutante Burlesque Showdown!</p>
  <p class="line intro" style="top:955px;margin:0">4 new burlesque sensassions strutting their stuff for the first time at THE SILVER GULL JAMBOREE</p>
  <p class="line intro" style="top:981px;margin:0">Be there or be squair Stjernekroken, Lindeløkka 17</p>
  <p class="line intro" style="top:1007px;margin:0">We do insist, dress to impress! Doors open at 18.00. Show start Rosa Quill at 19.00</p>

  <p class="fine-print" style="margin:0">CC:400,- Tickets sold at velvetlanternrevue.example. More information, VIP-tables, earlybirdtickets, etc : velvetlanternrevue.example. 20 år leg.plikt</p>
  <p class="web" style="margin:0">www.velvetlanternrevue.example</p>
</main>
</body>
</html>
```